Quiet Under Glass

Creation of a cover for a detective story
Size: 14 x 20.5 cm
Title: Quiet Under Glass
Author: Bastien Marchetaud
Publisher (at the bottom of the page): Editions Brunelle
Abstract: A surgeon in a hospital is faced with a series of post-operative infections. He suspects foul play due to the ongoing hostility of one of his colleagues.
Suggested Visual Elements:
- Hospital
- Operative room, with a surgeon and an African anesthetic
- Beautiful woman of 40 years old.
Target Market(s)
Adults
Industry/Entity Type
Book
Look and feel
Each slider illustrates characteristics of the customer's brand and the style your logo design should communicate.

```html
<!DOCTYPE html>
<html lang="en">
<head>
<meta charset="utf-8">
<title>Quiet Under Glass — Bastien Marchetaud</title>
<link rel="stylesheet" href="https://fonts.googleapis.com/css2?family=Big+Shoulders+Display:wght@800;900&family=Jost:wght@300&display=swap">
<style>
  :root {
    --backdrop: #f4f1ea;
    --theatre-deep: #0f2530;
    --theatre-mid: #24464f;
    --theatre-light: #4f7a7e;
    --scrub-teal: #5aa7a4;
    --signal-red: #d9383a;
    --band-red: rgba(226, 52, 55, 0.72);
    --paper: #ffffff;
    --ink: #1b1b1b;
  }
  * { margin: 0; padding: 0; box-sizing: border-box; }
  html, body { width: 900px; height: 1200px; overflow: hidden; background: var(--backdrop); }
  .cover {
    position: absolute; left: 68px; top: 40px;
    width: 765px; height: 1115px; overflow: hidden;
    background: var(--theatre-deep);
    box-shadow: 8px 10px 18px rgba(0, 0, 0, 0.25);
  }
  .cover-scene {
    position: absolute; inset: 0;
    background:
      radial-gradient(ellipse 55% 40% at 30% 40%, var(--scrub-teal) 0%, transparent 70%),
      radial-gradient(ellipse 45% 30% at 80% 72%, var(--theatre-light) 0%, transparent 70%),
      linear-gradient(180deg, var(--theatre-mid) 0%, var(--theatre-deep) 100%);
  }
  .cover-bands { position: absolute; inset: 0; }
  .author-plate {
    position: absolute; left: 183px; top: 68px; width: 397px; height: 65px;
    background: var(--signal-red);
    display: flex; align-items: center; justify-content: center;
    font-family: "Big Shoulders Display", sans-serif; font-weight: 800;
    font-size: 50px; letter-spacing: 1px; color: var(--paper);
    text-transform: lowercase; line-height: 1; white-space: nowrap;
  }
  .title {
    position: absolute; left: 70px; top: 618px; width: 500px;
    font-family: "Big Shoulders Display", sans-serif; font-weight: 900;
    font-size: 140px; color: var(--paper); text-transform: uppercase;
    line-height: 0.9; letter-spacing: -1px; white-space: nowrap;
  }
  .title-line { display: block; }
  .publisher {
    position: absolute; left: 307px; top: 1060px; width: 150px; height: 27px;
    background: var(--paper); color: var(--ink);
    font-family: "Jost", sans-serif; font-weight: 300; font-size: 17px;
    display: flex; align-items: center; justify-content: center; white-space: nowrap;
  }
</style>
</head>
<body>
<main class="cover">
  <div class="cover-scene" role="img" aria-label="Photograph of an operating theatre: a surgeon in teal scrubs and cap in the foreground, an anaesthetist and a woman behind him beside a patient monitor, surgical lamps overhead and instruments on a tray"></div>

  <svg class="cover-bands" width="765" height="1115" viewBox="0 0 765 1115" aria-hidden="true">
    <polygon points="765,284 765,381 420,530 395,470" fill="var(--band-red)"/>
    <polygon points="0,482 0,582 470,790 560,790" fill="var(--band-red)"/>
    <polygon points="0,882 0,950 330,950 330,882" fill="var(--band-red)" opacity="0.7"/>
  </svg>

  <div class="author-plate">Bastien Marchetaud</div>

  <h1 class="title">
    <span class="title-line">Quiet</span>
    <span class="title-line">Under</span>
    <span class="title-line">Glass</span>
  </h1>

  <div class="publisher">Editions Brunelle</div>
</main>
</body>
</html>
```